Banner Graphics For Quillo Storefront Page

Hello,
I am looking for a designer to help me with a banner heading that I want to place on my Quillo storefront page. My company sells outdoor kitchen/bbq island accessories. I would like for it to have a background photo with text/logo & graphics overlaid on the image. If possible I would like it to include the 5 small "benefit boxes" that are attached on the file that features graphics for one of the products that I sell . I have also included a color photo of my products in actual use. Feel free to use it but if you have a better idea of a background image feel free to try it, maybe a lifestyle stock photo?? Or maybe something else?? I am open to all ideas and you are the creative ones:) Feel free to be creative. The pixel requirements for final image is 3,000 pixels by 600 pixels. Let me know if you have any questions. THANKS! P.s. I also included some stock photos that I like to give you some ideas.

```html
<!DOCTYPE html>
<html lang="en">
<head>
<meta charset="utf-8">
<title>Crestline Outdoor Kitchens – Storefront Banner</title>
<link rel="stylesheet" href="https://fonts.googleapis.com/css2?family=Cinzel:wght@400;500&family=Libre+Caslon+Text:wght@400;700&family=Lato:wght@400;700;900&display=swap">
<style>
  :root {
    --ink-white: #ffffff;
    --photo-dark: #2a2420;
    --photo-mid: #4a3e35;
    --photo-warm: #6b5443;
    --photo-cool: #3b3a3d;
    --badge-border: #3fb8a8;
    --badge-top: #ffffff;
    --badge-label: #7d7f82;
    --badge-body: #1e1f21;
    --badge-shape: #2b2b2b;
  }
  * { box-sizing: border-box; margin: 0; padding: 0; }
  html, body { width: 1200px; height: 240px; overflow: hidden; background: var(--photo-dark); }
  .banner {
    position: relative;
    width: 1200px;
    height: 240px;
    overflow: hidden;
    font-family: "Lato", sans-serif;
    color: var(--ink-white);
  }
  .banner__photo {
    position: absolute;
    inset: 0;
    background:
      radial-gradient(ellipse at 30% 40%, rgba(120, 85, 60, 0.55), transparent 55%),
      radial-gradient(ellipse at 75% 60%, rgba(90, 80, 85, 0.5), transparent 60%),
      linear-gradient(100deg, var(--photo-warm) 0%, var(--photo-mid) 35%, var(--photo-cool) 65%, var(--photo-mid) 100%);
  }
  .banner__shade {
    position: absolute;
    inset: 0;
    background: rgba(20, 16, 14, 0.45);
  }
  .banner__frame {
    position: absolute;
    left: 40px;
    top: 30px;
    width: 1120px;
    height: 180px;
    border: 2px solid var(--ink-white);
  }

  .brand {
    position: absolute;
    left: 76px;
    top: 106px;
    width: 190px;
    display: flex;
    flex-direction: column;
    align-items: center;
    color: var(--ink-white);
  }
  .brand__name {
    font-family: "Cinzel", serif;
    font-weight: 400;
    font-size: 31px;
    line-height: 1;
    letter-spacing: 0.5px;
    white-space: nowrap;
  }
  .brand__rule {
    width: 176px;
    height: 1px;
    margin-top: 14px;
    background: var(--ink-white);
  }
  .brand__tagline {
    margin-top: 6px;
    font-family: "Libre Caslon Text", serif;
    font-weight: 400;
    font-size: 13px;
    line-height: 1;
    letter-spacing: 2.4px;
    white-space: nowrap;
  }

  .benefits {
    position: absolute;
    left: 348px;
    top: 82px;
    display: flex;
    gap: 16px;
  }
  .benefit {
    width: 53px;
    height: 74px;
    border: 1.5px solid var(--badge-border);
    border-radius: 5px;
    overflow: hidden;
    display: flex;
    flex-direction: column;
    background: var(--badge-body);
  }
  .benefit__icon {
    height: 32px;
    flex: none;
    background: var(--badge-top);
    display: flex;
    align-items: center;
    justify-content: center;
  }
  .benefit__label {
    height: 14px;
    flex: none;
    display: flex;
    align-items: center;
    justify-content: center;
    background: var(--badge-label);
    font-size: 6px;
    font-weight: 900;
    line-height: 6.2px;
    text-align: center;
    letter-spacing: 0.2px;
  }
  .benefit__text {
    flex: 1;
    padding: 3px 3px 0;
    font-size: 4.4px;
    line-height: 1.25;
    text-align: center;
  }

  .headline {
    position: absolute;
    left: 726px;
    top: 66px;
    width: 400px;
    text-align: center;
  }
  .headline__title {
    font-family: "Cinzel", serif;
    font-weight: 400;
    font-size: 36px;
    line-height: 1;
    letter-spacing: 1px;
    white-space: nowrap;
  }
  .headline__sub {
    margin-top: 10px;
    font-family: "Cinzel", serif;
    font-weight: 400;
    font-size: 27px;
    line-height: 1;
    white-space: nowrap;
  }
  .headline__line {
    margin-top: 8px;
    font-family: "Libre Caslon Text", serif;
    font-weight: 700;
    font-size: 17px;
    line-height: 1;
    white-space: nowrap;
  }
</style>
</head>
<body>
  <div class="banner">
    <div class="banner__photo" role="img" aria-label="Overhead lifestyle photo of a shared table with grilled dishes, salads, soups and plates passed between hands"></div>
    <div class="banner__shade"></div>
    <div class="banner__frame"></div>

    <div class="brand">
      <span class="brand__name">CRESTLINE</span>
      <span class="brand__rule"></span>
      <span class="brand__tagline">outdoor kitchens</span>
    </div>

    <div class="benefits">
      <div class="benefit">
        <div class="benefit__icon">
          <svg width="26" height="26" viewBox="0 0 26 26"><circle cx="13" cy="13" r="11" fill="none" stroke="var(--badge-shape)" stroke-width="2"/><rect x="3" y="10" width="20" height="6" fill="var(--badge-shape)"/></svg>
        </div>
        <div class="benefit__label">QUALITY</div>
        <div class="benefit__text">Our employees take pride in their work</div>
      </div>
      <div class="benefit">
        <div class="benefit__icon">
          <svg width="30" height="24" viewBox="0 0 30 24"><rect x="2" y="2" width="26" height="20" fill="none" stroke="var(--badge-shape)" stroke-width="1.5"/><rect x="5" y="6" width="20" height="5" fill="var(--badge-shape)"/><rect x="5" y="14" width="20" height="4" fill="var(--badge-shape)"/></svg>
        </div>
        <div class="benefit__label">VALUE</div>
        <div class="benefit__text">Our doors weight 10 pounds more than the competition</div>
      </div>
      <div class="benefit">
        <div class="benefit__icon">
          <svg width="32" height="24" viewBox="0 0 32 24"><rect x="2" y="3" width="28" height="18" fill="var(--badge-shape)"/><rect x="4" y="9" width="24" height="7" fill="var(--badge-top)"/></svg>
        </div>
        <div class="benefit__label">STRENGTH</div>
        <div class="benefit__text">Offers higher level of corrosion resistance</div>
      </div>
      <div class="benefit">
        <div class="benefit__icon">
          <svg width="32" height="24" viewBox="0 0 32 24"><rect x="2" y="3" width="12" height="18" fill="var(--badge-shape)"/><rect x="16" y="3" width="14" height="18" fill="none" stroke="var(--badge-shape)" stroke-width="1.5"/></svg>
        </div>
        <div class="benefit__label">DURABILITY</div>
        <div class="benefit__text">Thick and durable stainless steel construction</div>
      </div>
      <div class="benefit">
        <div class="benefit__icon">
          <svg width="26" height="26" viewBox="0 0 26 26"><circle cx="13" cy="13" r="11" fill="none" stroke="var(--badge-shape)" stroke-width="2"/><circle cx="13" cy="13" r="6" fill="var(--badge-shape)"/></svg>
        </div>
        <div class="benefit__label">PEACE OF<br>MIND</div>
        <div class="benefit__text">Your satisfaction is our highest priority</div>
      </div>
    </div>

    <div class="headline">
      <h1 class="headline__title">HAND CRAFTED</h1>
      <p class="headline__sub">BBQ/KITCHEN ACCESSORIES</p>
      <p class="headline__line">Elegant design with durable construction</p>
    </div>
  </div>
</body>
</html>
```